Web design for community centre - bright colours (provided) and matching existing logo

Website based on a provided logo and existing website template skeleton (it is a Wordpress theme we must use that is already installed)

Basically, see if you can improve the existing theme skeleton at https://tarvolnh.org.au/redesign/. Mostly we are looking for a much nicer menu that works with the logo, and a nice font/design for text content.

We have a developer who will work your design into the Wordpress theme – so you can get creative in a graphic software app and our developer can most likely implement your ideas.

The website ideally will include design ideas from the logo (e.g. the idea of people with their arms around each other, colours).

Improvement to the text displayed on the photo slider (e.g. a colour border or other decoration) is also needed.

It needs a 'community' feel.

Target Market(s)

Parents (provides childcare), older people, people with disabilities, recent migrants

Industry/Entity Type

Community Center

Number of Pages Required

1 page

Font styles to use
Sans Serif

Colors

Designer to choose colors to be used in the design.

Requirements
Must have
• A very aesthetic top menu. Nice use of spacing, negative space etc.
• Fonts need to be legally available without a pageview fee (one off purchase OK). You need to provide proof we can use the font legally.
• See https://www.pelmoray.org.au/ for an example of a menu we like.
• Must use the existing logo, provided in this brief.
• Needs to use colours from the logo but do not need to use all of them!
• Must be workable into the theme already installed at https://tarvolnh.org.au/redesign
Nice to have
• Maybe some kind of shapes attached to each menu link (top menu0
• A use of all 5 colours on the top menu, when you hover on it
Should not have
• Serif fonts

```html
<!DOCTYPE html>
<html lang="en">
<head>
<meta charset="utf-8">
<title>Tarvol Neighbourhood Learning Centre</title>
<link rel="stylesheet" href="https://fonts.googleapis.com/css2?family=Poppins:wght@300;400;500;600;700&display=swap">
<style>
:root{
  --green:#8cc63f;--pink:#ec1c79;--orange:#f7941d;--blue:#1cace3;--purple:#6a2c91;
  --ink:#111;--grey:#666;--band:#ebe9ea;--panel:#eeeeee;--dark:#333;--darker:#2b2b2b;
}
*{margin:0;padding:0;box-sizing:border-box}
html,body{width:1200px;height:2637px;overflow:hidden}
body{font-family:'Poppins',sans-serif;color:var(--ink);background:#fff;position:relative}
.abs{position:absolute}
.ph{position:absolute}
/* header */
.brand{left:94px;top:28px;display:flex;align-items:center;gap:12px}
.brand-dot{width:66px;height:66px;border-radius:50%;border:9px solid var(--blue)}
.brand-name{font-size:19px;font-weight:600;line-height:20px;color:#333;white-space:nowrap}
.brand-name span{display:block}
.search{left:855px;top:43px;width:249px;height:38px;border:1px solid #ccc;font-size:13px;padding:0 8px;display:flex;align-items:center;justify-content:space-between}
.nav{left:0;top:133px;width:1200px;height:31px}
.nav a{position:absolute;top:0;padding-top:14px;font-size:12.5px;font-weight:600;letter-spacing:.6px;color:#222;text-decoration:none;border-top:3px solid}
/* hero */
.hero-band{left:0;top:189px;width:1200px;height:577px;background:var(--band)}
.hero{left:92px;top:231px;width:1014px;height:493px;background:#fff}
.donate{left:700px;top:231px;width:406px;height:493px;text-align:center}
.donate h2{margin-top:208px;font-size:22px;font-weight:700;letter-spacing:.3px}
.donate p{font-size:14px;line-height:18px;margin:15px auto 0;width:300px;color:#222}
.donate .tax{display:inline-block;margin-top:28px;font-size:14px;font-weight:500;border-bottom:2px solid #222;padding-bottom:2px}
.pill{display:inline-block;margin-top:26px;background:var(--green);color:#fff;font-size:13px;font-weight:500;padding:8px 22px;border-radius:20px}
/* welcome */
.welcome{left:100px;top:840px;font-size:16px;font-weight:500}
.welcome i{display:inline-block;width:120px;height:1px;background:var(--pink);vertical-align:middle;margin-left:16px}
.w-title{left:100px;top:880px;font-size:33px;font-weight:700;line-height:34px}
.w-text{left:99px;top:963px;width:455px;font-size:14px;line-height:19.5px;color:var(--grey);font-weight:300}
.btn{position:absolute;color:#fff;font-size:14px;font-weight:500;display:flex;align-items:center;justify-content:center}
/* cards */
.card-text{position:absolute;background:var(--panel);padding:24px 16px}
.card-text h3{font-size:22px;font-weight:500;margin-top:8px}
.card-text p{font-size:12.5px;line-height:19.5px;color:#333;margin-top:8px}
.card-text .more{display:inline-block;margin-top:12px;background:var(--green);color:#fff;font-size:12.5px;font-weight:500;padding:5px 14px}
/* video */
.film{left:425px;top:1598px;width:630px;height:370px;background:var(--dark)}
.film-copy{left:700px;top:1680px;width:335px;text-align:center;color:#fff}
.film-copy h3{font-size:22px;font-weight:600}
.film-copy p{font-size:14.5px;line-height:19.5px;margin-top:20px}
.watch{display:inline-flex;align-items:center;gap:10px;margin-top:26px;background:var(--pink);font-size:14px;font-weight:500;padding:11px 18px 11px 28px}
/* newsletter */
.news{left:0;top:2026px;width:1200px;height:274px;background:#f5f5f7;text-align:center}
.news h2{margin-top:52px;font-size:25px;font-weight:500}
.news p{font-size:14.5px;line-height:22px;margin:12px auto 0;width:590px;color:#333}
.field{left:302px;top:2200px;width:601px;height:48px;border:1px solid #ccc;background:#fff;display:flex}
.field span{flex:1;font-size:14px;padding:13px 14px}
.field b{width:161px;background:var(--green);color:#fff;font-weight:400;font-size:17px;display:flex;align-items:center;justify-content:center}
/* footer */
.foot{left:0;top:2300px;width:1200px;height:337px;background:var(--dark);color:#ddd}
.foot-brand{left:94px;top:2352px;display:flex;align-items:center;gap:10px}
.foot-brand .brand-dot{width:60px;height:60px;border-color:#888}
.foot-brand .brand-name{color:#999}
.foot small{font-size:13px;line-height:18.5px}
.contact{left:543px;top:2457px;font-size:14px;line-height:25px;color:#fff}
.contact span{color:#bbb;font-size:13px}
.contact a{color:var(--pink);text-decoration:none;font-size:13px}
.badge{position:absolute;top:2349px;height:74px}
.social{position:absolute;top:2591px;width:30px;height:30px;border-radius:3px}
</style>
</head>
<body>

<header>
  <div class="abs brand"><span class="brand-dot"></span><span class="brand-name"><span>Tarvol</span><span>Neighbourhood</span><span>Learning Centre</span></span></div>
  <div class="abs search">Search
    <svg width="17" height="17" viewBox="0 0 17 17"><circle cx="7" cy="7" r="5.5" fill="none" stroke="#222" stroke-width="1.7"/><line x1="11" y1="11" x2="15.5" y2="15.5" stroke="#222" stroke-width="1.8"/></svg>
  </div>
  <nav class="abs nav">
    <a style="left:92px;border-color:var(--orange)">HOME</a>
    <a style="left:180px;border-color:var(--blue)">COURSES</a>
    <a style="left:288px;border-color:var(--green)">SOCIAL ENTERPRISE</a>
    <a style="left:464px;border-color:var(--pink)">COMMUNITY PROGRAMS</a>
    <a style="left:674px;border-color:var(--purple)">TARVOL CARES</a>
    <a style="left:798px;border-color:var(--orange)">VENUE HIRE</a>
    <a style="left:922px;border-color:var(--blue)">HOLLOWGATE CAFÉ</a>
  </nav>
</header>

<section>
  <div class="abs hero-band"></div>
  <div class="abs hero"></div>
  <div class="ph" role="img" aria-label="Adult students working at laptops in a bright classroom" style="left:92px;top:231px;width:608px;height:493px;background:linear-gradient(135deg,#e9e4dc,#c9b8a4 45%,#5a6f9a 80%,#d8d4d0)"></div>
  <div class="abs donate">
    <svg width="124" height="108" viewBox="0 0 124 108" style="position:absolute;left:142px;top:68px">
      <path d="M62 62 C40 44 30 34 30 22 C30 10 46 4 62 18 C78 4 94 10 94 22 C94 34 84 44 62 62Z" fill="var(--green)"/>
      <path d="M4 84 L22 70 C34 64 50 68 62 74 L84 74 C90 74 90 82 84 82 L62 82 L92 82 L116 66 C122 64 124 70 120 74 L92 98 C80 106 60 106 44 100 L22 96 Z" fill="var(--green)"/>
    </svg>
    <h2>Support us with a donation</h2>
    <p>Your donation will be directed towards the program of your choosing</p>
    <span class="tax">All donations tax deductible</span><br>
    <span class="pill">Donate Now</span>
  </div>
</section>

<section>
  <div class="abs welcome">Welcome to<i></i></div>
  <h1 class="abs w-title">Tarvol Neighbourhood<br>Learning Center</h1>
  <p class="abs w-text">It's hard to pinpoint just when Tarvol Cares began – a passing conversation at an art show, a new connection formed with a neighbouring organisation, and suddenly the Tarvol Centre, Marlow Lane Women's House, and Tarvol Baptist Church were sitting down in a room together.</p>
  <span class="btn" style="left:99px;top:1099px;width:140px;height:37px;background:var(--green)">Tarvol Cares</span>
  <span class="btn" style="left:251px;top:1099px;width:196px;height:37px;background:var(--pink)">View Course Brochure</span>
  <div class="ph" role="img" aria-label="Art student painting beside jars of brushes" style="left:622px;top:910px;width:232px;height:288px;background:linear-gradient(160deg,#8a7a62,#3b3f5c 55%,#1d1d24)"></div>
  <div class="ph" role="img" aria-label="Brick entrance of the learning centre under a clear sky" style="left:871px;top:846px;width:236px;height:352px;background:linear-gradient(180deg,#7da9d6 0%,#b8cde4 30%,#9c4b3c 55%,#6b4a38 80%,#5d7a45)"></div>
</section>

<section>
  <div class="ph" role="img" aria-label="Two smiling children leaning on an open book" style="left:92px;top:1273px;width:245px;height:255px;background:linear-gradient(180deg,#f4f2f0,#e6dcd2 60%,#c9b8a8)"></div>
  <div class="card-text" style="left:337px;top:1273px;width:250px;height:255px">
    <svg width="48" height="46" viewBox="0 0 48 46"><path d="M3 8 L22 4 L24 6 L26 4 L45 8 L45 42 L26 40 L24 42 L22 40 L3 42Z M24 6 V42 M8 14 H19 M8 20 H19 M8 26 H19 M29 14 H40 M29 20 H40 M29 26 H40" fill="none" stroke="#999" stroke-width="1.6"/></svg>
    <h3>Courses</h3>
    <p>100% of our profits help vulnerable learners in our community to participate in education and skill building activities.</p>
    <span class="more">View More</span>
  </div>
  <div class="ph" role="img" aria-label="Blue figures seated before a presenter at a whiteboard" style="left:610px;top:1273px;width:246px;height:255px;background:linear-gradient(180deg,#fafafa,#e8ecf4 55%,#6b8fd6)"></div>
  <div class="card-text" style="left:856px;top:1273px;width:250px;height:255px">
    <svg width="44" height="40" viewBox="0 0 44 40"><rect x="2" y="2" width="40" height="36" rx="2" fill="none" stroke="#999" stroke-width="1.6"/><line x1="2" y1="10" x2="42" y2="10" stroke="#999" stroke-width="1.6"/><path d="M17 18 L12 24 L17 30 M27 18 L32 24 L27 30 M24 17 L20 31" fill="none" stroke="#999" stroke-width="1.6"/></svg>
    <h3 style="margin-top:6px">Programs</h3>
    <p>Everyone welcome! &nbsp;The meeting is held &nbsp;at Tarvol Neighbourhood Learning Centre. &nbsp;Gold coin donation.</p>
    <span class="more">View More</span>
  </div>
</section>

<section>
  <div class="abs film"></div>
  <div class="ph" role="img" aria-label="Video still of the centre's entrance sign with a welcome title" style="left:179px;top:1625px;width:495px;height:315px;background:linear-gradient(170deg,#3d5a9c,#9fb4d8 30%,#b5334f 55%,#6f6a66 80%,#2a2a2a)"></div>
  <svg class="abs" style="left:416px;top:1753px" width="52" height="52" viewBox="0 0 52 52"><circle cx="26" cy="26" r="25" fill="rgba(0,0,0,.55)" stroke="#fff" stroke-width="2"/><path d="M21 16 L36 26 L21 36Z" fill="#fff"/></svg>
  <div class="abs" style="left:179px;top:1918px;width:495px;height:22px;background:rgba(0,0,0,.7);color:#fff;font-size:8px;padding:6px 0 0 72px">0:11 / 1:40</div>
  <div class="abs" style="left:179px;top:1917px;width:40px;height:2px;background:var(--pink)"></div>
  <div class="abs film-copy">
    <h3>TNLC Short films</h3>
    <p>Check out our new Streamly and Clipline channels! &nbsp;Now you can view all the amazing work that goes on at TNLC</p>
    <span class="watch">Watch Now <svg width="12" height="14" viewBox="0 0 12 14"><path d="M0 0 L12 7 L0 14Z" fill="#fff"/></svg></span>
  </div>
</section>

<section class="abs news">
  <h2>Sign up to our Newsletter</h2>
  <p>We send news about our courses, community programs, child care, cafe &amp; special events approximately 10 times a year.</p>
</section>
<div class="abs field"><span>Email Id:</span><b>Subscribe</b></div>

<footer>
  <div class="abs foot"></div>
  <div class="abs" style="left:518px;top:2300px;width:1px;height:267px;background:#555"></div>
  <div class="abs" style="left:0;top:2567px;width:1200px;height:1px;background:#444"></div>
  <div class="abs foot-brand"><span class="brand-dot"></span><span class="brand-name"><span>Tarvol</span><span>Neighbourhood</span><span>Learning Centre</span></span></div>
  <small class="abs" style="left:93px;top:2446px;width:380px;color:#ccc">Tarvol Neighbourhood Learning Centre Inc is registered as a charity with the National Community Charities Register ABN 51 903 227 614</small>
  <span class="badge" style="left:549px;width:131px;background:#1b3f8f"></span>
  <span class="badge" style="left:691px;width:136px;background:#fff"></span>
  <span class="badge" style="left:838px;width:98px;background:#fff"></span>
  <div class="abs contact">
    Address: <span>4-16 Marlow St, Tarvol, VIC, 3190</span><br>
    Phone: <span>03 9000 4172</span><br>
    Email Id: <a>admin@tarvolnh.org.au</a>
  </div>
  <small class="abs" style="left:95px;top:2584px;color:#ccc">© 2019 Tarvol Neighbourhood Learning Centre. All Rights Reserved.<br>Policies &amp; Procedures.</small>
  <span class="abs" style="left:825px;top:2596px;font-size:14px;color:#fff">Social Media:</span>
  <span class="social" style="left:941px;background:#3b5998"></span>
  <span class="social" style="left:981px;background:#3f729b"></span>
  <span class="social" style="left:1020px;background:#35465c"></span>
  <span class="social" style="left:1059px;background:#1ab7ea"></span>
</footer>

</body>
</html>
```